Harwick Downs Lamb Sticker Design

We need to create a design for sticky labels that will be placed meat packaging of individual cuts of meat for Harwick Downs Lamb.

These sticke...

Target Market(s)

People who purchase Gourmet Meat Products. Higher income, Age 35-65

Industry/Entity Type

Farming

Requirements
Must have
• The Harwick Downs Lamb Logo (attached)
• Quality Grass Fed Lamb
• Need to create a look of premium quality product.
• Space to write Net Weight
• Space to write $

```html
<!DOCTYPE html>
<html lang="en">
<head>
<meta charset="utf-8">
<title>Harwick Downs Lamb – Price Stickers</title>
<link rel="stylesheet" href="https://fonts.googleapis.com/css2?family=Caveat+Brush&family=Josefin+Sans:wght@700&family=Lobster&family=Lobster+Two:ital,wght@1,700&family=Playfair+Display:wght@700&display=swap">
<style>
  :root {
    --page: #ffffff;
    --frame-line: #d9d9d9;
    --tan: #b09676;
    --charcoal: #24282f;
    --crimson: #a8141c;
    --ink: #1e1410;
    --white: #ffffff;
  }
  html, body {
    margin: 0;
    padding: 0;
    width: 1200px;
    height: 1200px;
    overflow: hidden;
    background: var(--page);
  }
  .sticker-sheet { display: block; width: 1200px; height: 1200px; }
  .sheet-border { fill: none; stroke: var(--frame-line); stroke-width: 2; }
  .die-cut { fill: var(--white); stroke: var(--frame-line); stroke-width: 5; }
  .die-cut-fill { fill: var(--white); }
  .tan-fill { fill: var(--tan); }
  .charcoal-fill { fill: var(--charcoal); }
  .gold-fill { fill: url(#gold-foil); }
  .crest-face { fill: var(--white); stroke: var(--ink); stroke-width: 4; }
  .brand-name {
    font-family: "Josefin Sans", sans-serif;
    font-weight: 700;
    font-size: 46px;
    letter-spacing: 3px;
    fill: var(--ink);
    text-anchor: middle;
  }
  .weight-label {
    font-family: "Lobster Two", cursive;
    font-style: italic;
    font-weight: 700;
    font-size: 38px;
  }
  .currency {
    font-family: "Playfair Display", serif;
    font-weight: 700;
    font-size: 84px;
    fill: var(--white);
    text-anchor: middle;
  }
  .price {
    font-family: "Caveat Brush", cursive;
    font-size: 92px;
    fill: #111111;
    text-anchor: middle;
  }
  .tagline {
    font-family: "Lobster", cursive;
    font-size: 35px;
    text-anchor: middle;
  }
  .tan-text { fill: var(--tan); }
  .crimson-text { fill: var(--crimson); }
  .tan-star { fill: var(--tan); }
  .crimson-star { fill: var(--crimson); }
</style>
</head>
<body>
<svg class="sticker-sheet" viewBox="0 0 1500 1500" xmlns="http://www.w3.org/2000/svg">
  <defs>
    <linearGradient id="gold-foil" x1="0" y1="0" x2="1" y2="0.25">
      <stop offset="0" stop-color="#f0a830"/>
      <stop offset="0.3" stop-color="#f6c400"/>
      <stop offset="0.55" stop-color="#fbd800"/>
      <stop offset="0.8" stop-color="#a87a22"/>
      <stop offset="1" stop-color="#f3c800"/>
    </linearGradient>
    <path id="star" d="M0,-17 L4,-5.5 L16.2,-5.3 L6.5,2.1 L10,13.8 L0,6.8 L-10,13.8 L-6.5,2.1 L-16.2,-5.3 L-4,-5.5 Z"/>
  </defs>

  <rect class="sheet-border" x="28" y="28" width="1440" height="1438"/>

  <!-- Charcoal & tan sticker -->
  <g class="sticker sticker--charcoal">
    <circle class="die-cut" cx="418" cy="447" r="283"/>
    <polygon class="die-cut" points="172,580 662,580 662,1335 418,1142 172,1335"/>
    <circle class="die-cut-fill" cx="418" cy="447" r="280"/>
    <polygon class="die-cut-fill" points="175,575 659,575 659,1329 418,1138 175,1329"/>

    <polygon class="tan-fill" points="188,580 646,580 646,1300 418,1126 188,1300"/>
    <polygon class="charcoal-fill" points="218,625 616,625 616,1240 418,1090 218,1240"/>
    <circle class="tan-fill" cx="418" cy="447" r="267"/>
    <circle class="crest-face" cx="418" cy="449" r="233"/>
    <text class="brand-name" x="418" y="420">HARWICK</text>
    <text class="brand-name" x="418" y="475">DOWNS</text>
    <text class="brand-name" x="418" y="530">LAMB</text>

    <rect x="250" y="733" width="336" height="98" rx="10" fill="var(--white)" stroke="var(--tan)" stroke-width="4"/>
    <text class="weight-label tan-text" x="262" y="773">Net Weight:</text>

    <rect class="tan-fill" x="250" y="851" width="337" height="100" rx="10"/>
    <rect x="327" y="855" width="256" height="92" rx="8" fill="var(--white)"/>
    <text class="currency" x="290" y="933">$</text>
    <text class="price" x="452" y="932">39,99</text>

    <text class="tagline tan-text" x="418" y="1007">Quality Grass Fed Lamb</text>
    <g class="tan-star">
      <use href="#star" x="320" y="1048"/>
      <use href="#star" x="368" y="1048"/>
      <use href="#star" x="417" y="1048"/>
      <use href="#star" x="465" y="1048"/>
      <use href="#star" x="514" y="1048"/>
    </g>
  </g>

  <!-- Gold & crimson sticker -->
  <g class="sticker sticker--gold">
    <circle class="die-cut" cx="1062" cy="447" r="283"/>
    <polygon class="die-cut" points="816,580 1306,580 1306,1335 1062,1142 816,1335"/>
    <circle class="die-cut-fill" cx="1062" cy="447" r="280"/>
    <polygon class="die-cut-fill" points="819,575 1303,575 1303,1329 1062,1138 819,1329"/>

    <polygon class="gold-fill" points="832,580 1290,580 1290,1300 1062,1126 832,1300"/>
    <polygon points="870,628 1253,628 1253,1234 1062,1088 870,1234" fill="var(--white)" stroke="var(--crimson)" stroke-width="14" stroke-linejoin="miter"/>
    <circle class="gold-fill" cx="1062" cy="447" r="267"/>
    <circle class="crest-face" cx="1062" cy="449" r="233"/>
    <text class="brand-name" x="1062" y="420">HARWICK</text>
    <text class="brand-name" x="1062" y="475">DOWNS</text>
    <text class="brand-name" x="1062" y="530">LAMB</text>

    <text class="weight-label crimson-text" x="893" y="763">Net Weight:</text>
    <line x1="896" y1="822" x2="1229" y2="822" stroke="var(--crimson)" stroke-width="4"/>

    <rect x="894" y="845" width="338" height="113" rx="12" fill="var(--crimson)"/>
    <rect x="972" y="849" width="256" height="105" rx="10" fill="var(--white)"/>
    <text class="currency" x="934" y="931">$</text>
    <text class="price" x="1098" y="932">39,99</text>

    <text class="tagline crimson-text" x="1062" y="1007">Quality Grass Fed Lamb</text>
    <g class="crimson-star">
      <use href="#star" x="964" y="1048"/>
      <use href="#star" x="1012" y="1048"/>
      <use href="#star" x="1061" y="1048"/>
      <use href="#star" x="1109" y="1048"/>
      <use href="#star" x="1158" y="1048"/>
    </g>
  </g>
</svg>
</body>
</html>
```